Hi
Thank you for considering my job.

I need a layout design for a website. The design should preferably suit GlowcraftSkin Wordpress layout. Please design according to the attached LAYOUT.GIF

I already have a logo which I like but could be pushed to change if you have an exceptional design. Otherwise I would like to try to incorporate the jigsaw pieces in the design somehow.

Our company is based in Australia and called Harbor Ledger. We have developed a "Calm Folio" to assist both men and women going through divorce to prepare themselves adequately before the seek legal or financial advice to ensure they pay professionals for "advice" and not instructions on basic administration.

I hope the successful candidate will also be able to design a logo and squeeze page and all of the marketing images I will need to accompany The Calm Folio in a few weeks time, though it is not part of this job.

I have attached a very rough guide as to the types of elements and how I would like it to feel. I am not set on any of the fonts or general presentation at all. I feel comfortable with the colour scheme but again, open to ideas. Although the logo has the dark teal green background, I am not sure this works on the web page - open to ideas.

Some must haves:
a video on the front page
an opt in/members' login
link to Quillory books sales (affiliate widget)
Disclaimer must be visible on first SCREEN

The website must portray a professional, trustworthy and up to date type image - similar to a law firm, accounting firm, bank or university. It must be clean and crisp, inviting and non-gender biased.

Please message me if you have any questions at all.

Thanks again.
Marjorie
Perth, Australia

Target Market(s)

Australian MEN AND WOMEN - 30 - 60 years middle to upper income earners

Industry/Entity Type

Accounting

Requirements
Must have
• Some must haves:
a video on the front page
an opt in/members' login

The website must portray a professional, trustworthy and up to date type image - similar to a law firm, accounting firm BUT SLIGHTLY MORE PEOPLE ORIENTED

```html
<!DOCTYPE html>
<html lang="en">
<head>
<meta charset="utf-8">
<title>Harbor Ledger – Home</title>
<link href="https://fonts.googleapis.com/css2?family=Arimo:ital,wght@0,400;0,700;1,400&display=swap" rel="stylesheet">
<style>
:root{
  --taupe:#766c66;
  --taupe-dark:#5f5650;
  --divider:#a59c96;
  --lime:#cddd22;
  --teal:#014c58;
  --teal-text:#0d5560;
  --panel:#ececec;
  --red:#e1261c;
  --white:#ffffff;
  --ink:#444444;
  --muted:#666666;
}
*{box-sizing:border-box;margin:0;padding:0}
html,body{width:1200px;height:1000px;overflow:hidden;background:var(--white);font-family:"Arimo",Arial,sans-serif;color:var(--ink)}
.page{position:relative;width:1200px;height:1000px;overflow:hidden}
.abs{position:absolute}
h2{font-weight:400}

/* top bar */
.utility-links{left:28px;top:89px;display:flex;gap:21px;font-size:13px;color:var(--muted);white-space:nowrap}
.brand-square{left:76px;top:132px;width:40px;height:40px;background:var(--teal)}
.brand-name{left:76px;top:180px;font-size:33px;line-height:36px;color:var(--teal);white-space:nowrap;letter-spacing:-.3px}
.brand-tagline{left:77px;top:214px;font-size:15px;line-height:18px;color:var(--teal-text);white-space:nowrap}
.quote{left:440px;top:164px;width:318px;text-align:center;font-style:italic;font-size:13px;line-height:17px;color:#777;white-space:nowrap}
.cart-icon{left:985px;top:120px}
.cart-text{left:1032px;top:129px;font-size:14px;white-space:nowrap}
.cart-text .label{color:var(--lime)}
.cart-text .count{color:var(--teal)}
.main-links{top:217px;font-size:18px;line-height:22px;color:var(--teal);white-space:nowrap}
.main-links .current{color:var(--lime)}
.social{top:207px;display:flex;gap:3px}
.social span{display:flex;align-items:center;justify-content:center;width:26px;height:28px;background:var(--teal);color:var(--white);font-size:5px}

/* navigation band */
.nav-nub{left:1160px;top:278px;width:40px;height:36px;border-radius:50% 0 0 50%;background:var(--taupe)}
.nav-band{left:0;top:258px;width:1166px;height:75px;background:var(--taupe);border-bottom:2px solid var(--taupe-dark)}
.nav-item{top:258px;height:73px;display:flex;align-items:center;padding-left:24px;color:var(--white);font-size:18px;line-height:21px;letter-spacing:.6px;border-left:1px solid var(--divider);white-space:nowrap}
.nav-end{left:785px;top:258px;width:1px;height:73px;background:var(--divider)}
.search-field{left:811px;top:281px;width:226px;height:31px;background:var(--white);border:1px solid #ccc}
.search-btn{left:1037px;top:281px;width:82px;height:31px;background:var(--lime);color:var(--white);font-weight:700;font-size:16px;display:flex;align-items:center;justify-content:center}

/* side column */
.side-panel{left:940px;top:333px;width:260px;height:577px;background:var(--panel)}
.steps{left:966px;top:385px;width:183px;height:50px;background:var(--white);display:flex;justify-content:space-around;align-items:flex-end;padding-bottom:2px;font-size:12px;font-weight:700;color:#1a82b4;text-align:center;line-height:12px}
.steps small{display:block;font-size:5px;font-weight:400;color:#555;line-height:6px}
.steps .dot{display:block;margin:0 auto 2px;width:18px;height:18px;border-radius:50%;background:#3aa9d8}
.steps .dot.warm{background:#f2c230}
.steps .arrow{color:#8fd3ef;align-self:center;font-size:16px}
.book-cover{left:992px;top:452px;width:162px;height:108px;background:linear-gradient(135deg,#177a86,#0c4f5a);transform:skewY(8deg)}
.hot{left:1119px;top:476px;width:56px;height:56px;border-radius:50%;background:var(--red);color:var(--white);font-weight:700;font-size:12px;text-align:center;line-height:13px;padding-top:15px;transform:rotate(-20deg)}
.price{left:963px;top:582px;font-size:22px;line-height:26px;font-weight:700;color:var(--red)}
.side-cart{left:1130px;top:573px}
.side-copy{left:963px;top:616px;font-size:13px;line-height:17px;color:var(--teal);white-space:nowrap}
.read-more{left:963px;top:751px;font-size:16px;line-height:19px;font-weight:700;color:var(--teal);text-decoration:underline}
.book-shelf{left:962px;top:784px;width:206px;height:58px;background:linear-gradient(90deg,#6a6a6a,#2a3a48,#c49a2c,#3a3a3a,#8a1a1a,#304450)}

/* feature kit */
.folio-nub{left:52px;top:696px;width:47px;height:32px;border-radius:50%;background:var(--lime)}
.folio{left:25px;top:364px;width:322px;height:338px;background:var(--lime)}
.folio h2{position:absolute;left:13px;top:10px;font-size:20px;font-weight:700;color:var(--taupe-dark)}

/* video */
.how-title{left:415px;top:391px;font-size:20px;line-height:24px;color:var(--teal);white-space:nowrap}
.how-title b{font-weight:700}
.video-frame{left:388px;top:421px;width:552px;height:282px;background:var(--taupe);border-radius:22px 0 0 22px}
.video-nub{left:911px;top:443px;width:40px;height:46px;border-radius:50%;background:var(--white)}
.player{left:415px;top:443px;width:396px;height:237px;background:#111}
.player-bar{position:absolute;left:0;top:0;width:100%;height:16px;display:flex;justify-content:space-between;align-items:center;padding:0 6px;font-size:7px;color:#ddd}
.player-screen{position:absolute;left:0;top:16px;width:100%;height:203px;background:radial-gradient(circle at 45% 45%,#fafafa,#d6d6d6)}
.player-controls{position:absolute;left:0;bottom:0;width:100%;height:18px;display:flex;align-items:center;gap:10px;padding:0 10px;font-size:7px;color:#aaa}
.player-controls .tri{width:0;height:0;border-left:7px solid #ccc;border-top:4px solid transparent;border-bottom:4px solid transparent}
.video-caption{left:823px;top:593px;font-size:17px;line-height:22px;color:var(--white);white-space:nowrap}

/* lower blocks */
.tools-title{left:50px;top:756px;font-size:20px;line-height:24px;color:var(--teal);white-space:nowrap}
.tools-box{left:25px;top:784px;width:322px;height:126px;background:var(--teal);border-radius:18px 18px 0 0}
.articles-title{left:419px;top:756px;font-size:20px;line-height:24px;color:var(--teal);white-space:nowrap}
.articles-box{left:388px;top:784px;width:422px;height:126px;background:var(--teal);border-radius:18px 18px 0 0;padding:22px 0 0 30px;color:var(--white);font-size:13px;line-height:17px;letter-spacing:.2px;white-space:nowrap}
.articles-box .date{font-size:17px}

/* footer */
.footer{left:0;top:910px;width:1200px;height:65px;background:var(--taupe)}
.articles-nub{left:726px;top:904px;width:48px;height:34px;border-radius:50%;background:var(--teal)}
.footer-links{top:936px;font-size:18px;line-height:22px;color:var(--white);white-space:nowrap}
.footer-links.current{color:var(--lime)}
.footer-social{left:1090px;top:925px;display:flex;gap:4px}
.footer-social span{display:flex;align-items:center;justify-content:center;width:37px;height:38px;background:var(--teal);color:var(--white);font-size:6px}
.copyright{left:0;top:975px;width:1200px;height:25px;background:var(--taupe-dark);color:#6f6660;font-size:15px;text-align:center;line-height:25px;white-space:nowrap}
</style>
</head>
<body>
<div class="page">
  <nav class="abs utility-links"><span>Register</span><span>Login</span><span>Delivery</span><span>Checkout</span><span>My Account</span></nav>

  <span class="abs brand-square"></span>
  <div class="abs brand-name">Harbor Ledger</div>
  <div class="abs brand-tagline">working through it piece by piece</div>

  <p class="abs quote">“...Harbor Ledger helped me work though<br>everything, one step at a time.”</p>

  <svg class="abs cart-icon" width="40" height="31" viewBox="0 0 40 31"><path d="M2 3h7l5 17h19l4-12H12" fill="none" stroke="#766c66" stroke-width="3"/><circle cx="16" cy="27" r="3" fill="#766c66"/><circle cx="30" cy="27" r="3" fill="#766c66"/></svg>
  <div class="abs cart-text"><span class="label">Shopping Cart:</span> <span class="count">0 items</span></div>

  <span class="abs main-links current" style="left:810px">Home</span>
  <span class="abs main-links" style="left:888px">Tool</span>
  <span class="abs main-links" style="left:951px">FAQs</span>
  <span class="abs main-links" style="left:1027px">About Us</span>
  <div class="abs social" style="left:1120px"><span>Friendloop</span><span>Chirpline</span></div>

  <div class="abs nav-nub"></div>
  <div class="abs nav-band"></div>
  <div class="abs nav-item" style="left:25px">CONSIDERING<br>DIVORCE?</div>
  <div class="abs nav-item" style="left:197px">LEGAL<br>PROCESS</div>
  <div class="abs nav-item" style="left:337px">PARENTING</div>
  <div class="abs nav-item" style="left:484px">PROPERTY<br>&amp; FINANCE</div>
  <div class="abs nav-item" style="left:633px">COMMUNITY</div>
  <span class="abs nav-end"></span>
  <span class="abs search-field"></span>
  <span class="abs search-btn">Search</span>

  <aside class="abs side-panel"></aside>
  <div class="abs steps">
    <div><span class="dot"></span>Ask<small>a Question</small></div>
    <span class="arrow">»</span>
    <div><span class="dot"></span>Expert<small>Answers</small></div>
    <span class="arrow">»</span>
    <div><span class="dot warm"></span>Accept<small>if Satisfied</small></div>
  </div>
  <div class="abs book-cover" role="img" aria-label="Cover of the Harbor Ledger separation guide ebook"></div>
  <div class="abs hot">HOT<br>PRICE</div>
  <div class="abs price">$12.99</div>
  <svg class="abs side-cart" width="38" height="31" viewBox="0 0 38 31"><path d="M2 3h7l5 16h18l4-11H12" fill="none" stroke="#cddd22" stroke-width="3"/><circle cx="16" cy="26" r="3" fill="#cddd22"/><circle cx="29" cy="26" r="3" fill="#cddd22"/></svg>
  <p class="abs side-copy">Download immediately.<br>This simple guide provides a<br>wealth of essential information<br>and answers to your questions.<br>Advice and tips to help you get<br>a grip on all the changes in<br>your life.</p>
  <a class="abs read-more">Read more</a>
  <div class="abs book-shelf" role="img" aria-label="Row of book covers from the Quillory bookstore widget"></div>

  <div class="abs folio-nub"></div>
  <section class="abs folio"><h2>The Calm Folio:</h2></section>

  <h2 class="abs how-title"><b>harborledger</b> - How it Works</h2>
  <div class="abs video-frame"></div>
  <div class="abs video-nub"></div>
  <div class="abs player">
    <div class="player-bar"><span>Studiofold.com - How it Works</span><span>Clipstream</span></div>
    <div class="player-screen" role="img" aria-label="Video still on a crumpled paper background"></div>
    <div class="player-controls"><span class="tri"></span><span>0:00 / 2:04</span></div>
  </div>
  <p class="abs video-caption">Working<br>through it<br>piece<br>by piece.</p>

  <h2 class="abs tools-title">Try our free divorce tools:</h2>
  <section class="abs tools-box"></section>

  <h2 class="abs articles-title">Feature Articles:</h2>
  <section class="abs articles-box"><span class="date">21st of September:</span> Lorem ipsum dolor sit amet,<br>consectetur adipiscing elit. Mauris fringilla blandit mi nec<br>molestie. Aliquam non volutpat justo. Aliquam sit amet<br>ultricies ante, in condimentum felis. Praesent venenatis<br>sodales est, vel facilisis libero pulvinar id.</section>

  <footer class="abs footer"></footer>
  <div class="abs articles-nub"></div>
  <span class="abs footer-links current" style="left:25px">Home</span>
  <span class="abs footer-links" style="left:103px">Tool</span>
  <span class="abs footer-links" style="left:166px">FAQs</span>
  <span class="abs footer-links" style="left:242px">About Us</span>
  <div class="abs footer-social"><span>Friendloop</span><span>Chirpline</span></div>
  <div class="abs copyright">Copyright 2013 HarborLedger. Use of this website constitutes acceptance of User Agreement and Privacy Policy.</div>
</div>
</body>
</html>
```